The World Most Wanted Eyelahes

1. We need a web design for a new company based in California, USA
2. We are the manufacturer for 100% human hair eyelashes,
made in Indonesia.
3. We recently launched "Tapered Eyelashes" with human hair.
Currently, none of the people carried Tapered eyelash.
4. We would like to see designs that use the 4 different colors that match with my products as "Four Seasons" concepts.
5. We prefer to follow www.quelmo.com style, like professional website.
6. Focus on products as a manufacturer, therefore, all wholesaler and retailer copy and paste to their marketing tools.
7. Need bilingual English and Spanish.
8. Easy to link with social media.

Target Market(s)

United States and Central/South America.

Industry/Entity Type

Hair

Number of Pages Required

5+ page

Requirements
Must have
• 1. Details of Products with image.
• 2. Hottest/Newest Items "Tapered in 100% Human Hair"
• 3. Store Page
Nice to have
• 1. My competitors is Vintrel Eyelash. http://www.vintrellashes.com/
• Please follow the concepts of it.
• 2. www.Quelmo.com: They have great products detail on the website.
• i would like to focus on "Tapered" for new styles of the eyelash.
• 3. I want to visitors can write down the "Reviews" in every single product.
• Please check the www.PRUBCosmetics.com.
Should not have
• It's not salon/Shop for the beauty.
• No need an appointment.
• We are the manufacturer of the eyelash.

```html
<!DOCTYPE html>
<html lang="en">
<head>
<meta charset="utf-8">
<title>Lumette Eyelashes</title>
<link href="https://fonts.googleapis.com/css2?family=Raleway:wght@300;400;500;600;700&family=Great+Vibes&display=swap" rel="stylesheet">
<style>
:root{
  --backdrop:#141414;
  --page:#ffffff;
  --ink:#2b2b2b;
  --muted:#6d6d6d;
  --gold:#bf8d3c;
  --nav:#2f2d2a;
  --card:#f3f3f3;
  --footer:#3a3a3a;
  --footer-deep:#2d2d2d;
  --footer-text:#a9a9a9;
  --light:#e9e9e9;
}
*{margin:0;padding:0;box-sizing:border-box}
html,body{width:1171px;height:1200px;overflow:hidden;background:var(--backdrop);font-family:'Raleway',sans-serif;color:var(--ink)}
.site{position:absolute;left:148px;top:0;width:874px;height:1200px;background:var(--page)}
.abs{position:absolute}
.logo{left:28px;top:22px;font-size:56px;font-weight:400;letter-spacing:1px;color:var(--ink);line-height:1}
.toplinks{right:24px;top:18px;display:flex;gap:22px;font-size:13px;font-weight:500;color:var(--ink)}
.toplinks span{display:flex;align-items:center;gap:6px}
.search{left:522px;top:54px;width:236px;height:36px;border:1px solid #dcdcdc;font-size:12px;color:#aaa;padding:11px 0 0 17px;letter-spacing:.5px}
.search svg{position:absolute;right:14px;top:9px}
.cart{left:778px;top:54px}
.cart-label{left:820px;top:59px;font-size:10px;font-weight:600;line-height:1.3}
.cart-label b{color:var(--gold);font-size:13px}
.nav{left:9px;top:111px;width:857px;height:44px;background:var(--nav);color:#fff;font-size:13px;font-weight:500}
.nav div{position:absolute;top:0;height:44px;line-height:44px;text-align:center}
.nav .active{background:var(--gold);font-weight:700}
.nav .rule{width:1px;height:24px;top:10px;background:#6a6660}
.hero{left:9px;top:154px;width:857px;height:464px;background:linear-gradient(90deg,#1d2128 0%,#4a3640 32%,#a8356e 52%,#c94e9e 72%,#9c3f8f 100%)}
.hero .pack{left:434px;top:249px;width:146px;height:171px;border-radius:18px;background:linear-gradient(160deg,#e8dde8,#8b2e76);opacity:.85}
.script{font-family:'Great Vibes',cursive;color:#fff;line-height:1}
.h1{left:433px;top:46px;font-size:50px}
.h2{left:433px;top:96px;font-size:64px}
.tag1{left:433px;top:184px;font-size:19px;font-weight:300;color:#fff;letter-spacing:.2px}
.tag2{left:433px;top:210px;font-size:19px;font-weight:700;color:#fff}
.feat{left:603px;top:302px;color:#fff}
.feat h3{font-size:14px;font-weight:700;margin-bottom:9px}
.feat li{list-style:none;font-size:13px;font-weight:500;margin-bottom:9px;display:flex;align-items:center;gap:8px}
.feat li:before{content:"";width:9px;height:9px;border-radius:50%;background:#fff}
.dots{left:26px;top:422px;display:flex;gap:6px}
.dots i{width:15px;height:15px;border-radius:50%;background:#ddd;display:block}
.dots i.on{background:none;border:2px solid #fff}
.card{top:628px;width:209px;height:218px;background:var(--card);text-align:center}
.card h4{margin-top:20px;font-size:15px;font-weight:500;color:#555}
.card.hl h4{color:var(--gold);font-weight:700}
.card p{font-size:10px;color:#555;margin-top:4px}
.card .pack{width:110px;height:150px;margin:14px auto 0;border-radius:16px}
.footer{left:0;top:863px;width:874px;height:220px;background:var(--footer);color:var(--footer-text)}
.col{top:45px}
.col h5{font-size:15px;font-weight:500;color:#d8d8d8;margin-bottom:12px}
.col a{display:block;font-size:10px;color:var(--footer-text);text-decoration:none;margin-bottom:10px}
.social{display:flex;gap:9px}
.social i{width:23px;height:23px;background:#4a4a4a;display:block}
.social i.on{background:#1da1f2}
.email{width:221px;height:34px;background:#fff;font-size:10px;color:#777;padding:12px 0 0 16px}
.btn{margin-top:13px;width:112px;height:28px;background:var(--gold);color:#fff;font-size:12px;font-weight:700;line-height:28px;padding-left:16px}
.bottom{left:0;top:1083px;width:874px;height:117px;background:var(--footer-deep);color:var(--light)}
.copy{left:23px;top:36px;font-size:12px}
.legal{left:23px;top:65px;font-size:13px;font-weight:300;display:flex;gap:26px}
.logo-foot{right:22px;top:22px;font-size:60px;color:#fff;font-weight:400;letter-spacing:1px}
</style>
</head>
<body>
<div class="site">
  <div class="abs logo">LUMETTE</div>
  <div class="abs toplinks">
    <span><svg width="12" height="11" viewBox="0 0 12 11"><path d="M6 11 1 6A3 3 0 0 1 6 2a3 3 0 0 1 5 4z" fill="#bf8d3c"/></svg>WISHLIST</span>
    <span><svg width="12" height="12" viewBox="0 0 12 12"><circle cx="6" cy="6" r="4" fill="none" stroke="#bf8d3c" stroke-width="3" stroke-dasharray="2 1.2"/></svg>MY ACCOUNT</span>
    <span><svg width="11" height="12" viewBox="0 0 11 12"><circle cx="5.5" cy="3.5" r="3" fill="#bf8d3c"/><path d="M0 12a5.5 5 0 0 1 11 0z" fill="#bf8d3c"/></svg>LOGIN</span>
  </div>
  <div class="abs search">SEARCH SITE<svg width="18" height="18" viewBox="0 0 18 18"><circle cx="7.5" cy="7.5" r="6" fill="none" stroke="#bf8d3c" stroke-width="1.5"/><path d="M12 12l5 5" stroke="#bf8d3c" stroke-width="1.5"/></svg></div>
  <svg class="abs cart" width="34" height="36" viewBox="0 0 34 36"><rect x="1" y="5" width="32" height="30" rx="2" fill="#bf8d3c"/><path d="M9 12a8 7 0 0 0 16 0" fill="none" stroke="#fff" stroke-width="1.5"/></svg>
  <div class="abs cart-label">ITEMS<br>( <b>0</b> )</div>

  <div class="abs nav">
    <div style="left:0;width:208px">NEWEST ITEMS</div>
    <div class="rule" style="left:208px"></div>
    <div style="left:208px;width:149px">STORE</div>
    <div class="rule" style="left:357px"></div>
    <div style="left:357px;width:149px">BLOG</div>
    <div class="active" style="left:506px;width:174px">ABOUT US</div>
    <div style="left:680px;width:177px">CONTACT</div>
  </div>

  <div class="abs hero" role="img" aria-label="Close-up beauty portrait with long lashes beside a pink orchid on a magenta bokeh background">
    <div class="abs pack" role="img" aria-label="Boxed eyelash product package"></div>
    <div class="abs script h1">Handmade with</div>
    <div class="abs script h2">premium hair</div>
    <div class="abs tag1">COMPORTABLE WITH NATURAL AND SOFT</div>
    <div class="abs tag2">YOU LOOK MORE PERFECT WITH LUMETTE</div>
    <div class="abs feat"><h3>FACINATING YOUR EYES</h3><ul><li>Lorem ipsum dolor sit ampet</li><li>Ipsum dolor sit ampet</li><li>Dolor sit ampet</li></ul></div>
    <div class="abs dots"><i></i><i></i><i class="on"></i><i></i></div>
  </div>

  <div class="abs card" style="left:9px"><h4>SPARKLING YOUR EYES</h4><p>Lorem ipsum dolor sit ampet</p><div class="pack" role="img" aria-label="Gold eyelash package" style="background:linear-gradient(160deg,#e9c27a,#8a4a1a)"></div></div>
  <div class="abs card hl" style="left:225px"><h4>BLOSSOM YOUR EYES</h4><p>Lorem ipsum dolor sit ampet</p><div class="pack" role="img" aria-label="Pink eyelash package" style="background:linear-gradient(160deg,#f4d4dc,#c7878f)"></div></div>
  <div class="abs card" style="left:440px"><h4>FACINATING YOUR EYES</h4><p>Lorem ipsum dolor sit ampet</p><div class="pack" role="img" aria-label="Magenta eyelash package" style="background:linear-gradient(160deg,#e6b6d6,#8b2e76)"></div></div>
  <div class="abs card" style="left:657px"><h4>DAZZLING YOUR EYES</h4><p>Lorem ipsum dolor sit ampet</p><div class="pack" role="img" aria-label="Light blue eyelash package" style="background:linear-gradient(160deg,#e3eef4,#8fb1c8)"></div></div>

  <div class="abs footer">
    <div class="abs col" style="left:28px"><h5>ABOUT US</h5><a>About LUMETTE</a><a>How We Innovate</a><a>Jobs</a><a>Where to Buy</a></div>
    <div class="abs col" style="left:226px"><h5>SUPPORT</h5><a>Lorem ipsum</a><a>Dolor sit ampet</a><a>Lorem ipsum Dolor</a><a>Dolor sit ampet</a></div>
    <div class="abs col" style="left:429px"><h5>SOCIAL MEDIA</h5><div class="social"><i></i><i class="on"></i><i></i><i></i></div></div>
    <div class="abs col" style="left:631px"><h5>NEWSLETTER</h5><div class="email">EMAIL ADDRESS</div><div class="btn">SUBSCRIBE &rsaquo;</div></div>
  </div>
  <div class="abs bottom">
    <div class="abs copy">© 2015 Lumette LTD. All Rights Reserved.</div>
    <div class="abs legal"><span>PRIVACY &amp; SECURITY</span><span>SITE MAP</span><span>TERMS &amp; CONDITIONS</span></div>
    <div class="abs logo-foot">LUMETTE</div>
  </div>
</div>
</body>
</html>
```